Volren Goods Ltd Stationery Design Project

hi we need to design business cards, letter head, complimentary slips, scribble pads, note pads, envelopes for volren goods ltd.

please see business cards details

Kelvin Obutu

P.O Box 41873 -00312 Nairobi - Kenya
Tel: +254-733-218-904
Email: volrengoods@mailvexo.com

company name should appear on all stationery : Volren Goods Ltd

Industry/Entity Type

Business

Requirements
Must have
• kindly stick to colours in the logo

```html
<!DOCTYPE html>
<html lang="en">
<head>
<meta charset="utf-8">
<title>Volren Goods Ltd – Business Card</title>
<link href="https://fonts.googleapis.com/css2?family=Arvo:wght@400;700&display=swap" rel="stylesheet">
<style>
  :root {
    --backdrop: #e6e6e4;
    --card: #ffffff;
    --ink: #2f2f2f;
    --brand-orange: #f0901e;
    --brand-navy: #1f2a7a;
    --ornament-light: #ececec;
    --ornament-mid: #dcdcdc;
  }
  * { margin: 0; padding: 0; box-sizing: border-box; }
  html, body {
    width: 1200px;
    height: 938px;
    overflow: hidden;
    background: var(--backdrop);
    font-family: "Arvo", Georgia, serif;
    color: var(--ink);
  }
  .business-card {
    position: absolute;
    left: 390px;
    top: 119px;
    width: 420px;
    height: 700px;
    background: var(--card);
    box-shadow: 0 6px 22px rgba(0, 0, 0, 0.12);
    overflow: hidden;
  }
  .ornament {
    position: absolute;
  }
  .ornament-top {
    left: 10px;
    top: 0;
    width: 361px;
    height: 133px;
    border-radius: 0 0 50% 50% / 0 0 70% 70%;
    background: radial-gradient(ellipse at 50% 10%, var(--ornament-mid), var(--ornament-light) 70%, transparent 100%);
  }
  .ornament-corner {
    right: 0;
    bottom: 0;
    width: 130px;
    height: 221px;
    border-radius: 100% 0 0 0 / 60% 0 0 0;
    background: radial-gradient(ellipse at 100% 60%, var(--ornament-mid), var(--ornament-light) 70%, transparent 100%);
  }
  .brand {
    position: absolute;
    left: 0;
    right: 0;
    top: 252px;
    display: flex;
    align-items: center;
    justify-content: center;
    gap: 12px;
  }
  .brand-dot {
    width: 22px;
    height: 22px;
    border-radius: 50%;
    background: var(--brand-orange);
  }
  .brand-name {
    font-weight: 700;
    font-size: 34px;
    letter-spacing: 1px;
    color: var(--brand-navy);
  }
  .contact-person {
    position: absolute;
    left: 93px;
    top: 394px;
  }
  .person-name {
    font-size: 29px;
    font-weight: 400;
    line-height: 1.2;
  }
  .person-email {
    display: flex;
    align-items: center;
    gap: 7px;
    margin-top: 4px;
    font-size: 14px;
  }
  .icon { flex: none; }
  .company-address {
    position: absolute;
    left: 0;
    right: 0;
    top: 614px;
    text-align: center;
    font-size: 14px;
    line-height: 1.5;
  }
  .address-phone {
    display: inline-flex;
    align-items: center;
    gap: 3px;
  }
</style>
</head>
<body>
  <main class="business-card">
    <div class="ornament ornament-top" role="img" aria-label="Light grey swirling flame ornament along the top edge"></div>
    <div class="ornament ornament-corner" role="img" aria-label="Light grey swirling sun ornament in the lower right corner"></div>

    <div class="brand">
      <span class="brand-dot"></span>
      <span class="brand-name">VOLREN GOODS</span>
    </div>

    <section class="contact-person">
      <h1 class="person-name">Kelvin Obutu</h1>
      <p class="person-email">
        <svg class="icon" width="17" height="12" viewBox="0 0 17 12" aria-hidden="true">
          <rect x="0" y="0" width="17" height="12" fill="var(--brand-orange)"/>
          <path d="M0 0 L8.5 7 L17 0" fill="none" stroke="#fff" stroke-width="1.4"/>
        </svg>
        volrengoods@mailvexo.com
      </p>
    </section>

    <address class="company-address" style="font-style: normal;">
      <div>P.O Box 41873 -00312 Nairobi - Kenya</div>
      <div class="address-phone">
        <svg class="icon" width="15" height="16" viewBox="0 0 15 16" aria-hidden="true">
          <rect x="0" y="1" width="4" height="14" rx="1" fill="var(--ink)"/>
          <rect x="5" y="3" width="10" height="12" rx="1" fill="var(--ink)"/>
          <rect x="7" y="5" width="6" height="3" fill="#fff"/>
          <rect x="7" y="10" width="2" height="2" fill="#fff"/>
          <rect x="11" y="10" width="2" height="2" fill="#fff"/>
        </svg>
        +254-733-218-904
      </div>
    </address>
  </main>
</body>
</html>
```